Upsell Vertical Banner Ad Design For B2B Marketing Agency Vertical 768px × 1180px IS THE SIZE

I need a banner made for my website www.brightlanepromotionhub.biz This banner will be an upsell advertisement for after someone signs up for my monthly program. When they login to their account for the 1st time I will give them the chance to upgrade their account to our annual program with just one click.

this is a page that upsells it currently to give you an idea how we market ourselves:
https://tlpx.pagevault-example.com/page/tlp-annual-upsell

Use this content:

Are You Ready To Commit To Taking Your Business To The Next Level?

Because We're In This For The Long-Haul and Dedicated To Your Success...

Save $300 By Upgrading To An Annual Membership And Pay Only $74/mth

((BUTTON))Yes, Upgrade My Plan Right Now!

*Must prepay the full year at only $898/yr!

Target Market(s)

business owners

Industry/Entity Type

Marketing

Requirements
Must have
• 768px × 1180px IS THE SIZE vertical

Use this content:

Nice to have
• Use this content:

Should not have
• Use this content:

```html
<!DOCTYPE html>
<html lang="en">
<head>
<meta charset="UTF-8">
<title>Bright Lane Promotion Hub — Annual Upgrade Banner</title>
<link rel="stylesheet" href="https://fonts.googleapis.com/css2?family=Bebas+Neue&family=Montserrat:wght@300;400;600;700&display=swap">
<style>
  :root {
    --backdrop: #9a9a9a;
    --paper: #f7f7f7;
    --brand-blue: #1176bd;
    --ink-grey: #4a4a4d;
    --road-grey: #56585b;
    --white: #f4f4f6;
  }
  * { box-sizing: border-box; margin: 0; padding: 0; }
  html, body {
    width: 812px; height: 1200px; overflow: hidden;
    background: var(--backdrop);
  }
  .banner {
    position: absolute; left: 47px; top: 48px;
    width: 718px; height: 1103px;
    background: var(--paper);
    box-shadow: 4px 6px 10px rgba(0,0,0,0.35);
    overflow: hidden;
  }
  .hero-art {
    position: absolute; left: 0; top: 0; width: 718px; height: 574px;
  }
  .brand {
    position: absolute; left: 30px; top: 44px;
    display: flex; align-items: center; gap: 12px;
  }
  .brand-mark {
    width: 20px; height: 20px; background: var(--brand-blue);
  }
  .brand-name {
    font-family: 'Montserrat', sans-serif; font-weight: 700;
    font-size: 24px; letter-spacing: 1px; color: var(--brand-blue);
  }
  .headline {
    position: absolute; left: 30px; top: 114px;
    font-family: 'Bebas Neue', sans-serif; font-weight: 400;
    line-height: 1;
  }
  .headline-lead { display: block; font-size: 56px; color: var(--brand-blue); letter-spacing: 0.5px; }
  .headline-mid { display: block; font-size: 43px; color: var(--ink-grey); margin-top: 6px; }
  .headline-key { display: block; font-size: 100px; color: var(--brand-blue); margin-top: 2px; }
  .offer {
    position: absolute; left: 0; top: 574px; width: 718px; height: 529px;
    background: var(--brand-blue);
    color: var(--white);
    font-family: 'Montserrat', sans-serif;
    text-align: center;
  }
  .offer-intro {
    position: absolute; left: 0; right: 0; top: 33px;
    font-weight: 600; font-size: 24.5px; line-height: 32px; letter-spacing: -0.3px;
  }
  .offer-saving {
    position: absolute; left: 0; right: 0; top: 122px;
    font-weight: 600; font-size: 93px; line-height: 1; letter-spacing: -1px;
  }
  .offer-terms {
    position: absolute; left: 0; right: 0; top: 220px;
    font-weight: 600; font-size: 37px; line-height: 47px; letter-spacing: 0.5px;
  }
  .upgrade-button {
    position: absolute; left: 45px; top: 397px; width: 627px; height: 65px;
    background: #ffffff; border-radius: 13px;
    display: flex; align-items: center; justify-content: center;
    color: var(--brand-blue); text-decoration: none;
    font-size: 31px; letter-spacing: -0.5px; white-space: nowrap;
  }
  .upgrade-button strong { font-weight: 700; margin-right: 8px; }
  .upgrade-button span { font-weight: 300; }
  .offer-footnote {
    position: absolute; left: 0; right: 0; top: 483px;
    font-weight: 300; font-size: 15px; line-height: 20px;
  }
</style>
</head>
<body>
  <main class="banner">
    <svg class="hero-art" viewBox="0 0 718 574" role="img" aria-label="Illustration of a grey road with blue edges rising into an upward arrow, with NEXT LEVEL painted on the asphalt">
      <defs>
        <linearGradient id="road-fade" x1="0" y1="0" x2="1" y2="1">
          <stop offset="0" stop-color="#f7f7f7"/>
          <stop offset="0.45" stop-color="#e6e6e7"/>
          <stop offset="1" stop-color="#56585b"/>
        </linearGradient>
      </defs>
      <rect width="718" height="574" fill="url(#road-fade)"/>
    </svg>

    <div class="brand">
      <span class="brand-mark"></span>
      <span class="brand-name">BRIGHT LANE PROMOTION HUB</span>
    </div>

    <h1 class="headline">
      <span class="headline-lead">Are You Ready To Commit</span>
      <span class="headline-mid">To Taking Your Business To The</span>
      <span class="headline-key">Next Level?</span>
    </h1>

    <section class="offer">
      <p class="offer-intro">Because We're In This For The Long-Haul<br>and Dedicated To Your Success...</p>
      <p class="offer-saving">SAVE $300</p>
      <p class="offer-terms">BY UPGRADING TO<br>AN ANNUAL MEMBERSHIP<br>AND PAY ONLY $74/MTH</p>
      <a class="upgrade-button" href="https://tlpx.pagevault-example.com/page/tlp-annual-upsell"><strong>YES, UPGRADE</strong><span>MY PLAN RIGHT NOW!</span></a>
      <p class="offer-footnote">*Must prepay the full year at only $898/yr!</p>
    </section>
  </main>
</body>
</html>
```